The Marlowe Legal Group, P.C.
Business Cards, Stationary & Email Signature & Letterhead
Use same font as used in my logo
Ruth Benning
Attorney
2847 Tamworth Lane
Suite 3405
Kennesaw, GA 30582
ruthbenningesq@quillpost.net
www.marlowelegaloffice.com
Logo + whatever
Ai file of my logo for Stationary project

```html
<!DOCTYPE html>
<html lang="en">
<head>
<meta charset="utf-8">
<title>The Marlowe Legal Group, P.C. — Stationery</title>
<link rel="stylesheet" href="https://fonts.googleapis.com/css2?family=Cinzel:wght@600&family=Lato:wght@400;700&display=swap">
<style>
  :root {
    --navy: #23409a;
    --navy-dark: #1c3482;
    --ink: #5d6270;
    --paper: #ffffff;
    --stage: #e8e6e2;
    --rule: #c9ccd4;
    --on-navy: #dfe5f5;
  }
  * { box-sizing: border-box; margin: 0; padding: 0; }
  html, body { width: 1200px; height: 866px; overflow: hidden; }
  body { background: var(--stage); font-family: "Lato", sans-serif; color: var(--ink); position: relative; }

  .sheet { position: absolute; background: var(--paper); box-shadow: 0 2px 8px rgba(0,0,0,.18); overflow: hidden; }

  .brand { display: flex; align-items: center; gap: 6px; color: var(--navy); font-family: "Cinzel", serif; font-weight: 600; line-height: 1.05; white-space: nowrap; }
  .brand-dot { border-radius: 50%; background: var(--navy); flex: none; }
  .divider { width: 1px; background: var(--rule); align-self: stretch; }
  .contact { font-size: 6px; line-height: 1.5; color: var(--ink); white-space: nowrap; }
  .contact .em { color: var(--navy); font-weight: 700; }

  /* letterhead */
  .letterhead { left: 96px; top: 168px; width: 444px; height: 624px; }
  .letterhead .head { position: absolute; left: 34px; top: 42px; display: flex; gap: 12px; }
  .letterhead .brand { font-size: 13px; }
  .letterhead .brand-dot { width: 26px; height: 26px; }

  /* business cards */
  .card { width: 188px; height: 102px; }
  .card-front .brand { position: absolute; left: 10px; top: 18px; font-size: 7px; gap: 5px; }
  .card-front .brand-dot { width: 14px; height: 14px; }
  .card-front .person { position: absolute; left: 100px; top: 14px; border-left: 1px solid var(--rule); padding-left: 6px; }
  .card-front .person-name { font-size: 7px; }
  .card-front .person-role { font-size: 5px; margin-bottom: 4px; }
  .card-front .contact { font-size: 5px; line-height: 1.5; }
  .person-name { font-family: "Cinzel", serif; font-weight: 600; font-size: 8px; color: var(--navy); white-space: nowrap; }
  .person-role { font-size: 6px; color: var(--ink); margin-bottom: 4px; }
  .card-front .bar { position: absolute; left: 0; right: 0; bottom: 8px; height: 8px; background: var(--navy); color: #fff; font-size: 5px; line-height: 8px; padding-left: 10px; }
  .card-back { background: var(--navy); }
  .card-back .brand { position: absolute; left: 0; right: 0; top: 34px; justify-content: center; color: #fff; font-size: 9px; }
  .card-back .brand-dot { width: 18px; height: 18px; background: #fff; }
  .card-back .web { position: absolute; left: 0; right: 0; bottom: 10px; text-align: center; color: var(--on-navy); font-size: 5.5px; letter-spacing: .5px; }

  /* envelopes */
  .envelope-back { left: 576px; top: 336px; width: 552px; height: 180px; }
  .envelope-back svg { position: absolute; inset: 0; }
  .envelope-front { left: 492px; top: 432px; width: 564px; height: 252px; }
  .envelope-front .head { position: absolute; left: 28px; top: 36px; display: flex; gap: 12px; }
  .envelope-front .brand { font-size: 12px; }
  .envelope-front .brand-dot { width: 24px; height: 24px; }

  /* email signature */
  .signature { left: 576px; top: 715px; width: 427px; height: 72px; }
  .signature .row { position: absolute; left: 14px; top: 10px; display: flex; gap: 12px; }
  .signature .brand { font-size: 10px; }
  .signature .brand-dot { width: 20px; height: 20px; }
  .signature .bar { position: absolute; left: 0; right: 0; bottom: 8px; height: 9px; background: var(--navy); color: #fff; font-size: 5.5px; line-height: 9px; padding-left: 14px; }
</style>
</head>
<body>

<section class="sheet letterhead">
  <div class="head">
    <div class="brand"><span class="brand-dot"></span><span>The Marlowe<br>Legal Group, P.C.</span></div>
    <span class="divider"></span>
    <div class="contact">2847 Tamworth Lane, Suite 3405<br>Kennesaw, GA 30582<br>Tel 770.555.0148<br>Fax 770.555.0149<br><span class="em">ruthbenningesq@quillpost.net</span></div>
  </div>
</section>

<section class="sheet card card-front" style="left:629px;top:72px;">
  <div class="brand"><span class="brand-dot"></span><span>The Marlowe<br>Legal Group, P.C.</span></div>
  <div class="person">
    <div class="person-name">Ruth Benning</div>
    <div class="person-role">Attorney</div>
    <div class="contact">Tel 770.555.0148<br>Fax 770.555.0149<br>ruthbenningesq@quillpost.net<br>2847 Tamworth Lane<br>Suite 3405, Kennesaw</div>
  </div>
  <div class="bar">www.marlowelegaloffice.com</div>
</section>
<section class="sheet card card-back" style="left:830px;top:72px;">
  <div class="brand"><span class="brand-dot"></span><span>The Marlowe<br>Legal Group, P.C.</span></div>
  <div class="web">www.marlowelegaloffice.com</div>
</section>
<section class="sheet card card-front" style="left:629px;top:192px;">
  <div class="brand"><span class="brand-dot"></span><span>The Marlowe<br>Legal Group, P.C.</span></div>
  <div class="person">
    <div class="person-name">Ruth Benning</div>
    <div class="person-role">Attorney</div>
    <div class="contact">Tel 770.555.0148<br>Fax 770.555.0149<br>ruthbenningesq@quillpost.net<br>2847 Tamworth Lane<br>Suite 3405, Kennesaw</div>
  </div>
  <div class="bar">www.marlowelegaloffice.com</div>
</section>
<section class="sheet card card-back" style="left:830px;top:192px;">
  <div class="brand"><span class="brand-dot"></span><span>The Marlowe<br>Legal Group, P.C.</span></div>
  <div class="web">www.marlowelegaloffice.com</div>
</section>

<section class="sheet envelope-back">
  <svg width="552" height="180" viewBox="0 0 552 180" aria-hidden="true">
    <polyline points="0,0 276,70 552,0" fill="none" stroke="#d7d9de" stroke-width="1"/>
    <polyline points="0,180 200,100" fill="none" stroke="#e2e4e8" stroke-width="1"/>
    <polyline points="552,180 352,100" fill="none" stroke="#e2e4e8" stroke-width="1"/>
    <circle cx="276" cy="46" r="14" fill="#23409a"/>
  </svg>
</section>

<section class="sheet envelope-front">
  <div class="head">
    <div class="brand"><span class="brand-dot"></span><span>The Marlowe<br>Legal Group, P.C.</span></div>
    <span class="divider"></span>
    <div class="contact">2847 Tamworth Lane, Suite 3405<br>Kennesaw, GA 30582<br>Tel 770.555.0148<br><span class="em">www.marlowelegaloffice.com</span></div>
  </div>
</section>

<section class="sheet signature">
  <div class="row">
    <div class="brand"><span class="brand-dot"></span><span>The Marlowe<br>Legal Group, P.C.</span></div>
    <span class="divider"></span>
    <div>
      <div class="person-name">Ruth Benning</div>
      <div class="person-role">Attorney</div>
    </div>
    <span class="divider"></span>
    <div class="contact">Tel 770.555.0148<br>2847 Tamworth Lane, Suite 3405<br>Kennesaw, GA 30582</div>
  </div>
  <div class="bar">www.marlowelegaloffice.com &nbsp;|&nbsp; ruthbenningesq@quillpost.net</div>
</section>

</body>
</html>
```